Banner Ad Design Project

We are a SEO company and need a banner design for our new service, the highlights being:

- Pay Per Performance SEO service
- Guaranteed Zumbly page 1 ranking
- Only $197 per month (+ performance bonus)

Can be all on one static banner or made into an animated GIF - designers choice...

Site URL (not up yet) will be RankNest412.com (by velHelm) - this is a spinoff site of our existing business, velHelm LLC - logo attached and should be included on the banner.

Industry/Entity Type

Business

Requirements
Must have
• Banner delivered in multiple sizes:
- 200 x 200
- 250 x 250
- 300 x 250
- 336 x 280
- 468 x 60
- 728 x 90
- 120 x 600
- 160 x 600

```html
<!DOCTYPE html>
<html lang="en">
<head>
<meta charset="utf-8">
<title>velHelm SEO banner set</title>
<link rel="stylesheet" href="https://fonts.googleapis.com/css2?family=Oswald:wght@400;500&display=swap">
<style>
:root{
  --backdrop:#2b2b2b;
  --navy-deep:#08245e;
  --navy:#10409a;
  --navy-bright:#1d5cc4;
  --seo-letter:#1f58c0;
  --accent-green:#8cc63f;
  --highlight:#ffd21f;
  --ink:#ffffff;
  --brand-ink:#1c3f8c;
  --button-top:#ffc93a;
  --button-bottom:#f29b0c;
  --panel:#ffffff;
}
*{box-sizing:border-box;margin:0;padding:0}
html,body{width:1200px;height:1000px;overflow:hidden}
body{background:var(--backdrop);position:relative;font-family:"Oswald",sans-serif}

.banner{position:absolute;overflow:hidden;background:var(--panel)}
.stage{position:absolute;background:
  radial-gradient(ellipse at 72% 85%,rgba(70,130,230,.55) 0%,rgba(29,92,196,.25) 35%,rgba(8,36,94,0) 70%),
  linear-gradient(160deg,var(--navy-deep) 0%,var(--navy) 50%,var(--navy-deep) 100%)}

.seo-visual{position:absolute;
  background:linear-gradient(to top,rgba(255,255,255,.95) 0%,rgba(235,241,252,.75) 45%,rgba(255,255,255,.0) 100%)}
.seo-word{position:absolute;left:0;right:0;bottom:18%;display:flex;justify-content:space-around;
  color:var(--seo-letter);font-weight:500;line-height:1}

.features{list-style:none;position:absolute;color:var(--ink);font-weight:400;letter-spacing:-.01em;line-height:1.2}
.features li{display:flex;align-items:flex-start}
.features em{font-style:normal;color:var(--highlight)}
.tick{flex:none;width:1em;height:1em;margin-right:.5em;margin-top:.1em}

.brand{position:absolute;display:flex;align-items:center;color:var(--brand-ink);font-weight:500;letter-spacing:-.01em;line-height:1}
.brand-dot{display:block;border-radius:50%;background:var(--accent-green);flex:none}

.cta{position:absolute;display:flex;align-items:center;justify-content:center;border-radius:4px;
  background:linear-gradient(var(--button-top),var(--button-bottom));color:var(--ink);font-weight:400;
  box-shadow:0 2px 2px rgba(0,0,0,.25);letter-spacing:.01em;white-space:nowrap}

.divider-v{position:absolute;top:0;bottom:0;background:var(--accent-green)}
.divider-h{position:absolute;left:0;right:0;background:var(--accent-green)}

/* 728 x 90 leaderboard */
.banner--leaderboard{left:243px;top:98px;width:728px;height:90px}
.banner--leaderboard .stage{left:200px;top:0;right:0;bottom:0}
.banner--leaderboard .divider-v{left:194px;width:6px}
.banner--leaderboard .brand{left:15px;top:21px;font-size:30px;gap:12px}
.banner--leaderboard .brand-dot{width:48px;height:48px}
.banner--leaderboard .features{left:237px;top:11px;font-size:14px}
.banner--leaderboard .features li{margin-bottom:4px}
.banner--leaderboard .seo-visual{left:492px;top:2px;width:118px;height:88px}
.banner--leaderboard .seo-word{font-size:26px;bottom:4px}
.banner--leaderboard .cta{left:622px;top:36px;width:94px;height:22px;font-size:12px}

/* 468 x 60 banner */
.banner--banner{left:481px;top:210px;width:468px;height:58px}
.banner--banner .stage{left:128px;top:0;right:0;bottom:0}
.banner--banner .divider-v{left:124px;width:4px}
.banner--banner .brand{left:10px;top:13px;font-size:18px;gap:8px}
.banner--banner .brand-dot{width:32px;height:32px}
.banner--banner .features{left:150px;top:7px;font-size:8.5px}
.banner--banner .features li{margin-bottom:5px}
.banner--banner .seo-visual{left:318px;top:2px;width:70px;height:56px}
.banner--banner .seo-word{font-size:16px;bottom:2px}
.banner--banner .cta{left:400px;top:22px;width:58px;height:14px;font-size:7.5px;border-radius:2px}

/* 160 x 600 wide skyscraper */
.banner--wide-sky{left:136px;top:233px;width:160px;height:600px}
.banner--wide-sky .stage{left:0;top:0;right:0;height:427px}
.banner--wide-sky .divider-h{top:427px;height:5px}
.banner--wide-sky .features{left:8px;top:30px;font-size:15px}
.banner--wide-sky .features li{margin-bottom:14px}
.banner--wide-sky .seo-visual{left:12px;top:210px;width:140px;height:217px}
.banner--wide-sky .seo-word{font-size:42px;bottom:30px}
.banner--wide-sky .brand{left:0;right:0;top:452px;flex-direction:column;font-size:28px;gap:6px}
.banner--wide-sky .brand-dot{width:56px;height:56px}
.banner--wide-sky .cta{left:24px;top:558px;width:112px;height:26px;font-size:14px}

/* 120 x 600 skyscraper */
.banner--sky{left:328px;top:234px;width:120px;height:598px}
.banner--sky .stage{left:0;top:0;right:0;height:434px}
.banner--sky .divider-h{top:434px;height:4px}
.banner--sky .features{left:5px;top:42px;font-size:12px;line-height:1.45}
.banner--sky .features li{margin-bottom:12px}
.banner--sky .features .small{font-size:10px}
.banner--sky .seo-visual{left:0;top:240px;width:120px;height:194px}
.banner--sky .seo-word{font-size:36px;bottom:28px}
.banner--sky .brand{left:0;right:0;top:450px;flex-direction:column;font-size:24px;gap:6px}
.banner--sky .brand-dot{width:48px;height:48px}
.banner--sky .cta{left:13px;top:551px;width:94px;height:22px;font-size:12px}

/* 336 x 280 large rectangle */
.banner--large-rect{left:481px;top:286px;width:337px;height:280px}
.banner--large-rect .stage{left:0;top:0;right:0;height:199px}
.banner--large-rect .divider-h{top:199px;height:4px}
.banner--large-rect .features{left:26px;top:27px;font-size:16px}
.banner--large-rect .features li{margin-bottom:14px}
.banner--large-rect .seo-visual{left:195px;top:40px;width:130px;height:159px}
.banner--large-rect .seo-word{font-size:40px;bottom:28px}
.banner--large-rect .brand{left:22px;top:219px;font-size:30px;gap:8px}
.banner--large-rect .brand-dot{width:46px;height:46px}
.banner--large-rect .cta{left:208px;top:230px;width:112px;height:26px;font-size:14px}

/* 250 x 250 square */
.banner--square{left:827px;top:316px;width:250px;height:250px}
.banner--square .stage{left:0;top:0;right:0;height:183px}
.banner--square .divider-h{top:183px;height:4px}
.banner--square .features{left:10px;top:24px;font-size:14px}
.banner--square .features li{margin-bottom:12px}
.banner--square .seo-visual{left:145px;top:10px;width:105px;height:173px}
.banner--square .seo-word{font-size:38px;bottom:46px}
.banner--square .brand{left:12px;top:198px;font-size:26px;gap:8px}
.banner--square .brand-dot{width:40px;height:40px}
.banner--square .cta{left:158px;top:209px;width:84px;height:20px;font-size:11px}

/* 300 x 250 medium rectangle */
.banner--medium-rect{left:481px;top:587px;width:300px;height:250px}
.banner--medium-rect .stage{left:0;top:0;right:0;height:179px}
.banner--medium-rect .divider-h{top:179px;height:4px}
.banner--medium-rect .features{left:16px;top:23px;font-size:14px}
.banner--medium-rect .features li{margin-bottom:12px}
.banner--medium-rect .seo-visual{left:165px;top:14px;width:130px;height:165px}
.banner--medium-rect .seo-word{font-size:40px;bottom:40px}
.banner--medium-rect .brand{left:10px;top:192px;font-size:30px;gap:8px}
.banner--medium-rect .brand-dot{width:44px;height:44px}
.banner--medium-rect .cta{left:182px;top:204px;width:104px;height:24px;font-size:14px}

/* 200 x 200 small square */
.banner--small-square{left:791px;top:636px;width:200px;height:200px}
.banner--small-square .stage{left:0;top:0;right:0;height:147px}
.banner--small-square .divider-h{top:147px;height:3px}
.banner--small-square .features{left:8px;top:20px;font-size:10px}
.banner--small-square .features li{margin-bottom:9px}
.banner--small-square .seo-visual{left:105px;top:22px;width:95px;height:125px}
.banner--small-square .seo-word{font-size:28px;bottom:30px}
.banner--small-square .brand{left:10px;top:160px;font-size:20px;gap:6px}
.banner--small-square .brand-dot{width:32px;height:32px}
.banner--small-square .cta{left:126px;top:168px;width:64px;height:15px;font-size:8px;border-radius:2px}
</style>
</head>
<body>

<svg width="0" height="0" style="position:absolute" aria-hidden="true">
  <defs>
    <symbol id="tick" viewBox="0 0 16 16">
      <rect x="1" y="4" width="11" height="11" fill="none" stroke="#ffd21f" stroke-width="1.5"/>
      <path d="M3 9 L6.5 12.5 L15 2" fill="none" stroke="#ffd21f" stroke-width="2.6" stroke-linecap="round" stroke-linejoin="round"/>
    </symbol>
  </defs>
</svg>

<!-- 728 x 90 -->
<section class="banner banner--leaderboard">
  <div class="brand"><span class="brand-dot"></span>velHelm</div>
  <div class="divider-v"></div>
  <div class="stage" role="img" aria-label="Deep blue sunburst rays background"></div>
  <ul class="features">
    <li><svg class="tick"><use href="#tick"/></svg><span>Pay Per Performance <em>SEO service</em></span></li>
    <li><svg class="tick"><use href="#tick"/></svg><span><em>Guaranteed</em> Zumbly page 1 ranking</span></li>
    <li><svg class="tick"><use href="#tick"/></svg><span><em>Only $197</em> per month (+ performance bonus)</span></li>
  </ul>
  <div class="seo-visual" role="img" aria-label="Illustration of three rising white arrows"><div class="seo-word"><span>S</span><span>E</span><span>O</span></div></div>
  <div class="cta">LEARN MORE</div>
</section>

<!-- 468 x 60 -->
<section class="banner banner--banner">
  <div class="brand"><span class="brand-dot"></span>velHelm</div>
  <div class="divider-v"></div>
  <div class="stage" role="img" aria-label="Deep blue sunburst rays background"></div>
  <ul class="features">
    <li><svg class="tick"><use href="#tick"/></svg><span>Pay Per Performance <em>SEO service</em></span></li>
    <li><svg class="tick"><use href="#tick"/></svg><span><em>Guaranteed</em> Zumbly page 1 ranking</span></li>
    <li><svg class="tick"><use href="#tick"/></svg><span><em>Only $197</em> per month (+ performance bonus)</span></li>
  </ul>
  <div class="seo-visual" role="img" aria-label="Illustration of three rising white arrows"><div class="seo-word"><span>S</span><span>E</span><span>O</span></div></div>
  <div class="cta">LEARN MORE</div>
</section>

<!-- 160 x 600 -->
<section class="banner banner--wide-sky">
  <div class="stage" role="img" aria-label="Deep blue sunburst rays background"></div>
  <ul class="features">
    <li><svg class="tick"><use href="#tick"/></svg><span>Pay Per Performance<br><em>SEO service</em></span></li>
    <li><svg class="tick"><use href="#tick"/></svg><span><em>Guaranteed</em> Zumbly<br>page 1 ranking</span></li>
    <li><svg class="tick"><use href="#tick"/></svg><span><em>Only $197</em> per month<br>(+ performance bonus)</span></li>
  </ul>
  <div class="seo-visual" role="img" aria-label="Illustration of three rising white arrows"><div class="seo-word"><span>S</span><span>E</span><span>O</span></div></div>
  <div class="divider-h"></div>
  <div class="brand"><span class="brand-dot"></span>velHelm</div>
  <div class="cta">LEARN MORE</div>
</section>

<!-- 120 x 600 -->
<section class="banner banner--sky">
  <div class="stage" role="img" aria-label="Deep blue sunburst rays background"></div>
  <ul class="features">
    <li><svg class="tick"><use href="#tick"/></svg><span>Pay Per Performance<br><em>SEO service</em></span></li>
    <li><svg class="tick"><use href="#tick"/></svg><span><em>Guaranteed</em> Zumbly<br>page 1 ranking</span></li>
    <li><svg class="tick"><use href="#tick"/></svg><span><em>Only $197</em> per month<br><span class="small">(+ performance bonus)</span></span></li>
  </ul>
  <div class="seo-visual" role="img" aria-label="Illustration of three rising white arrows"><div class="seo-word"><span>S</span><span>E</span><span>O</span></div></div>
  <div class="divider-h"></div>
  <div class="brand"><span class="brand-dot"></span>velHelm</div>
  <div class="cta">LEARN MORE</div>
</section>

<!-- 336 x 280 -->
<section class="banner banner--large-rect">
  <div class="stage" role="img" aria-label="Deep blue sunburst rays background"></div>
  <ul class="features">
    <li><svg class="tick"><use href="#tick"/></svg><span>Pay Per Performance<br><em>SEO service</em></span></li>
    <li><svg class="tick"><use href="#tick"/></svg><span><em>Guaranteed</em> Zumbly<br>page 1 ranking</span></li>
    <li><svg class="tick"><use href="#tick"/></svg><span><em>Only $197</em> per month<br>(+ performance bonus)</span></li>
  </ul>
  <div class="seo-visual" role="img" aria-label="Illustration of three rising white arrows"><div class="seo-word"><span>S</span><span>E</span><span>O</span></div></div>
  <div class="divider-h"></div>
  <div class="brand"><span class="brand-dot"></span>velHelm</div>
  <div class="cta">LEARN MORE</div>
</section>

<!-- 250 x 250 -->
<section class="banner banner--square">
  <div class="stage" role="img" aria-label="Deep blue sunburst rays background"></div>
  <ul class="features">
    <li><svg class="tick"><use href="#tick"/></svg><span>Pay Per Performance<br><em>SEO service</em></span></li>
    <li><svg class="tick"><use href="#tick"/></svg><span><em>Guaranteed</em> Zumbly<br>page 1 ranking</span></li>
    <li><svg class="tick"><use href="#tick"/></svg><span><em>Only $197</em> per month<br>(+ performance bonus)</span></li>
  </ul>
  <div class="seo-visual" role="img" aria-label="Illustration of three rising white arrows"><div class="seo-word"><span>S</span><span>E</span><span>O</span></div></div>
  <div class="divider-h"></div>
  <div class="brand"><span class="brand-dot"></span>velHelm</div>
  <div class="cta">LEARN MORE</div>
</section>

<!-- 300 x 250 -->
<section class="banner banner--medium-rect">
  <div class="stage" role="img" aria-label="Deep blue sunburst rays background"></div>
  <ul class="features">
    <li><svg class="tick"><use href="#tick"/></svg><span>Pay Per Performance<br><em>SEO service</em></span></li>
    <li><svg class="tick"><use href="#tick"/></svg><span><em>Guaranteed</em> Zumbly<br>page 1 ranking</span></li>
    <li><svg class="tick"><use href="#tick"/></svg><span><em>Only $197</em> per month<br>(+ performance bonus)</span></li>
  </ul>
  <div class="seo-visual" role="img" aria-label="Illustration of three rising white arrows"><div class="seo-word"><span>S</span><span>E</span><span>O</span></div></div>
  <div class="divider-h"></div>
  <div class="brand"><span class="brand-dot"></span>velHelm</div>
  <div class="cta">LEARN MORE</div>
</section>

<!-- 200 x 200 -->
<section class="banner banner--small-square">
  <div class="stage" role="img" aria-label="Deep blue sunburst rays background"></div>
  <ul class="features">
    <li><svg class="tick"><use href="#tick"/></svg><span>Pay Per Performance<br><em>SEO service</em></span></li>
    <li><svg class="tick"><use href="#tick"/></svg><span><em>Guaranteed</em> Zumbly<br>page 1 ranking</span></li>
    <li><svg class="tick"><use href="#tick"/></svg><span><em>Only $197</em> per month<br>(+ performance bonus)</span></li>
  </ul>
  <div class="seo-visual" role="img" aria-label="Illustration of three rising white arrows"><div class="seo-word"><span>S</span><span>E</span><span>O</span></div></div>
  <div class="divider-h"></div>
  <div class="brand"><span class="brand-dot"></span>velHelm</div>
  <div class="cta">LEARN MORE</div>
</section>

</body>
</html>
```